New website for out outstanding veterinary training center

We already have a beautiful logo with nice colors and we are now looking for a breathtaking modern website to present our training center and future corses held there. A section to book open courses should also be available.

We are planing the realize the website with Wordpress.
The following pages should be available:
- Startpage / Overview
- Page to present the different rooms and seating option
- Page where the rooms can be booked
- Page where recommended accommodation are presented
- Page to present and book corses
- contact page
- Impressum

Target Market(s)

European Union

Industry/Entity Type

Education, Veterinary medicine

Number of Pages Required

5+ page

Font styles to use
Sans Serif

Colors
00AB8E
00BBA5
67D7C9
C6EFE9
E9F9F6

Requirements
Must have
• The website must be clear and easy to read. The colors form the logos should be used for the design.
Should not have
• To playful design. The page is not for a veterinary practice. we are a training center for veterinarians!

```html
<!DOCTYPE html>
<html lang="en">
<head>
<meta charset="utf-8">
<title>Vetora Training Center</title>
<link href="https://fonts.googleapis.com/css2?family=Roboto:wght@400;500;700&family=Arimo:wght@400&display=swap" rel="stylesheet">
<style>
:root{
  --green:#17a085;
  --green-bright:#00ab8e;
  --green-soft:#67d7c9;
  --mint:#c6efe9;
  --mint-pale:#e9f9f6;
  --ink:#3a2f3a;
  --body:#555;
  --footer:#3d2b3a;
  --panel:#f5f5f5;
  --line:#e4e4e4;
}
*{margin:0;padding:0;box-sizing:border-box}
html,body{width:1200px;height:3897px;overflow:hidden;background:#fff}
body{position:relative;font-family:'Roboto',sans-serif;color:var(--ink)}
.abs{position:absolute}
.body-text{font-family:'Arimo',sans-serif;font-size:14px;color:var(--body)}
.btn{position:absolute;display:flex;align-items:center;justify-content:center;background:var(--green);color:#fff;font-family:'Roboto',sans-serif;font-size:15px;font-weight:500;text-decoration:none;border-radius:3px}
.section-title{position:absolute;left:0;width:1200px;text-align:center;font-size:30px;font-weight:400;text-transform:uppercase;color:var(--ink)}
.section-title span{color:var(--green)}
.rule{position:absolute;height:2px;width:44px;background:var(--ink)}
.rule.green{background:var(--green)}

/* header */
.header{position:absolute;left:0;top:0;width:1200px;height:154px;background:#fff;z-index:2;box-shadow:0 1px 3px rgba(0,0,0,.12)}
.brand-disc{position:absolute;left:107px;top:-2px;width:218px;height:230px;border-radius:0 0 109px 109px;background:#fff;z-index:3;display:flex;align-items:center;justify-content:center;flex-direction:column;gap:10px}
.brand-dot{width:70px;height:70px;border-radius:50%;background:var(--green)}
.brand-name{font-size:30px;font-weight:700;color:var(--ink)}
.nav{position:absolute;top:106px;font-size:15px;font-weight:500;color:var(--ink);z-index:3}
.nav.active{color:var(--green)}

/* hero */
.hero{position:absolute;left:0;top:154px;width:1200px;height:706px;background:linear-gradient(120deg,#d9dfe4 0%,#b7a58d 35%,#8b6a4a 55%,#3f7fa6 78%,#c9d4da 100%)}
.hero-title1{position:absolute;left:120px;top:344px;font-size:48px;font-weight:700;color:var(--green)}
.hero-title2{position:absolute;left:120px;top:404px;font-size:54px;font-weight:500;color:var(--ink)}

/* services */
.svc-head{position:absolute;font-size:21px;font-weight:500;color:var(--green)}
.svc-text{position:absolute;width:300px;line-height:21px;font-size:13px}
.right{text-align:right}

/* welcome */
.welcome-photo{position:absolute;left:0;top:1484px;width:595px;height:474px;background:linear-gradient(160deg,#e8dde2,#c9c6cc 55%,#8f8a88)}
.welcome-panel{position:absolute;left:595px;top:1484px;width:605px;height:474px;background:var(--panel)}

/* accommodation */
.accommodation{position:absolute;left:0;top:1958px;width:1200px;height:490px;background:radial-gradient(ellipse at 30% 20%,#2ab392,#1c9f81 60%,#179579)}

/* courses */
.card{position:absolute;top:2584px;width:308px;height:448px;background:#fff;border:1px solid #e6e6e6;box-shadow:0 1px 4px rgba(0,0,0,.08)}
.card-photo{height:226px}
.badge{position:absolute;left:218px;top:194px;width:70px;height:70px;border-radius:50%;background:var(--green);color:#fff;font-size:17px;font-weight:500;display:flex;align-items:center;justify-content:center}
.stars{position:absolute;left:20px;top:267px;font-size:13px;color:#666;letter-spacing:1px}
.card-title{position:absolute;left:24px;top:298px;width:270px;font-size:18px;line-height:31px;color:var(--ink)}
.card-rule{position:absolute;left:16px;right:16px;top:377px;height:1px;background:var(--line)}
.avatar{position:absolute;left:17px;top:390px;width:50px;height:50px;border-radius:50%;background:linear-gradient(135deg,#b98c6e,#6b4b3a)}
.author{position:absolute;left:77px;top:405px;font-size:17px}
.card-link{position:absolute;right:14px;top:407px;font-size:14px;font-weight:500;color:var(--green)}

/* newsletter */
.newsletter{position:absolute;left:0;top:3108px;width:1200px;height:395px;background:linear-gradient(135deg,#f3ede3,#f7f4ee 50%,#eee8de)}
.email{position:absolute;left:227px;top:3301px;width:746px;height:55px;border:1px solid #bbb;background:#fff;font-family:'Arimo',sans-serif;font-size:14px;color:#666;padding-left:20px;display:flex;align-items:center}

/* footer */
.footer{position:absolute;left:0;top:3503px;width:1200px;height:394px;background:var(--footer)}
.foot-nav{position:absolute;top:3736px;font-size:15px;font-weight:500;color:#fff;transform:translateX(-50%)}
.social{position:absolute;top:3782px;width:36px;height:36px;border:2px solid #fff;border-radius:50%}
</style>
</head>
<body>

<header class="header"></header>
<div class="brand-disc"><div class="brand-dot"></div><div class="brand-name">Vetora</div></div>
<a class="btn" style="left:932px;top:26px;width:156px;height:48px;border-radius:24px;z-index:3">BOOK COURSE</a>
<nav>
  <div class="nav active" style="left:467px">HOME</div>
  <div class="nav" style="left:557px">ABOUT US</div>
  <div class="nav" style="left:676px">SERVICES</div>
  <div class="nav" style="left:793px">COURSES</div>
  <div class="nav" style="left:906px">NEWS</div>
  <div class="nav" style="left:996px">CONTACT US</div>
</nav>

<section class="hero" role="img" aria-label="Veterinarian examining a husky on a clinic table"></section>
<div class="hero-title1">Vetora</div>
<div class="hero-title2">Training Center</div>
<a class="btn" style="left:128px;top:493px;width:140px;height:49px">READ MORE</a>

<h2 class="section-title" style="top:920px">Our <span>Services</span></h2>
<div class="rule green" style="left:578px;top:966px"></div>
<p class="abs body-text" style="left:0;width:1200px;text-align:center;top:984px">Sed ut perspiciatis unde omnis iste natus error sit voluptatem accusantium doloremque</p>

<svg class="abs" style="left:420px;top:1056px" width="360" height="360" viewBox="0 0 360 360">
  <circle cx="180" cy="180" r="162" fill="none" stroke="#17a085" stroke-width="4"/>
  <circle cx="180" cy="180" r="82" fill="#17a085"/>
  <text x="180" y="189" text-anchor="middle" font-family="Roboto, sans-serif" font-size="26" font-weight="700" fill="#ffffff">Vetora</text>
  <g fill="#fff" stroke="#17a085" stroke-width="4">
    <circle cx="66" cy="73" r="47"/><circle cx="305" cy="73" r="47"/>
    <circle cx="66" cy="287" r="47"/><circle cx="305" cy="287" r="47"/>
  </g>
  <g fill="none" stroke="#3a2f3a" stroke-width="2.5" stroke-linecap="round">
    <path d="M54 73h24M66 61v24"/>
    <path d="M292 80c0-10 26-10 26 0-4 8-22 8-26 0z"/>
    <rect x="55" y="272" width="22" height="30" rx="2"/><path d="M60 284h12M60 292h12"/>
    <path d="M299 275h12v6h6v12h-6v6h-12v-6h-6v-12h6z"/>
  </g>
</svg>

<div class="svc-head" style="right:787px;top:1072px">SERVICES 01</div>
<p class="svc-text body-text right" style="left:110px;top:1114px">Sed ut perspiciatis unde omnis iste natus error sit voluptatem accusantium</p>
<div class="svc-head" style="left:797px;top:1072px">SERVICES 02</div>
<p class="svc-text body-text" style="left:797px;top:1114px">Sed ut perspiciatis unde omnis iste natus error sit voluptatem accusantium</p>
<div class="svc-head" style="right:787px;top:1287px">SERVICES 03</div>
<p class="svc-text body-text right" style="left:110px;top:1329px">Sed ut perspiciatis unde omnis iste natus error sit voluptatem accusantium</p>
<div class="svc-head" style="left:797px;top:1287px">SERVICES 04</div>
<p class="svc-text body-text" style="left:797px;top:1329px">Sed ut perspiciatis unde omnis iste natus error sit voluptatem accusantium</p>

<div class="welcome-photo" role="img" aria-label="Clinic waiting room with staff and owners greeting dogs"></div>
<section class="welcome-panel"></section>
<h2 class="abs" style="left:641px;top:1551px;font-size:30px;font-weight:400">WELCOME TO <span style="color:var(--green)">VETORA</span></h2>
<div class="rule" style="left:643px;top:1601px;width:50px"></div>
<p class="abs body-text" style="left:646px;top:1624px;width:430px;line-height:29.2px;font-size:13.5px;text-align:justify">Sed ut perspiciatis unde omnis iste natus error sit voluptatem accusan tium doloremque laudantium, totam rem aperiam, eaque ipsa quae ab inventore veritatis et quasi architecto beatae vitae dicta sunt explicabo. Nemo enim ipsam voluptatem quia voluptas sit aspernatur aut odit aut fugit, sed quia consequuntur magni dolores eos qui ratione voluptatem sequi nesciunt.Neque porro quisquam est, qui dolorem ipsum quia dolor sit amet, consectetur, adipisci velit, sed quia</p>
<a class="btn" style="left:646px;top:1849px;width:130px;height:47px">READ MORE</a>

<section class="accommodation" role="img" aria-label="Green tinted close-up of a pet paw"></section>
<h2 class="section-title" style="top:2083px;color:#fff;font-size:33px">Recommended Accommodation</h2>
<div class="rule" style="left:577px;top:2142px;background:#fff;width:46px"></div>
<p class="abs body-text" style="left:220px;width:760px;top:2163px;text-align:center;line-height:29px;color:#fff;font-size:13.5px">Sed ut perspiciatis unde omnis iste natus error sit voluptatem accusantium doloremque laudantium, totam rem aperiam, eaque ipsa quae ab illo inventore veritatis et quasi architecto beatae vitae dicta sunt explicabo. Nemo enim ipsam aut sed quia consequuntur magni dolores eos qui ratione voluptatem sequi nesciunt.</p>
<a class="btn" style="left:514px;top:2271px;width:170px;height:52px;background:transparent;border:2px solid #fff;font-size:18px">READ MORE</a>

<h2 class="section-title" style="top:2502px">Latest <span>Courses</span></h2>
<div class="rule" style="left:574px;top:2555px;width:52px"></div>

<article class="card" style="left:112px">
  <div class="card-photo" role="img" aria-label="Vet holding a golden puppy" style="background:linear-gradient(135deg,#f2f2f2,#e6d3b5 60%,#d9c8ad)"></div>
  <div class="badge">FREE</div>
  <div class="stars">☆☆☆☆☆ (05 REVIEWS)</div>
  <div class="card-title">Sed ut perspiciatis unde omnis iste natus error</div>
  <div class="card-rule"></div>
  <div class="avatar" role="img" aria-label="Instructor portrait"></div>
  <div class="author">Lena Hart</div>
  <div class="card-link">READ MORE</div>
</article>
<article class="card" style="left:446px">
  <div class="card-photo" role="img" aria-label="Vet in blue scrubs holding a tabby cat" style="background:linear-gradient(135deg,#2e6c94,#5c8fb0 50%,#a99a86)"></div>
  <div class="badge">FREE</div>
  <div class="stars">☆☆☆☆☆ (05 REVIEWS)</div>
  <div class="card-title">Sed ut perspiciatis unde omnis iste natus error</div>
  <div class="card-rule"></div>
  <div class="avatar" role="img" aria-label="Instructor portrait"></div>
  <div class="author">Lena Hart</div>
  <div class="card-link">READ MORE</div>
</article>
<article class="card" style="left:781px">
  <div class="card-photo" role="img" aria-label="Vet with tablet beside a labrador" style="background:linear-gradient(135deg,#2b5d63,#6e8e8c 50%,#e3d8c4)"></div>
  <div class="badge">FREE</div>
  <div class="stars">☆☆☆☆☆ (05 REVIEWS)</div>
  <div class="card-title">Sed ut perspiciatis unde omnis iste natus error</div>
  <div class="card-rule"></div>
  <div class="avatar" role="img" aria-label="Instructor portrait"></div>
  <div class="author">Lena Hart</div>
  <div class="card-link">READ MORE</div>
</article>

<section class="newsletter" role="img" aria-label="Faded background of a puppy resting on a hand"></section>
<h2 class="section-title" style="top:3154px">Newsletter <span>Signup</span></h2>
<p class="abs body-text" style="left:280px;width:640px;top:3225px;text-align:center;line-height:27px;font-size:13.5px">Sed ut perspiciatis unde omnis iste natus error sit voluptatem accusantium doloremque laudantium, inventore veritatis et quasi architecto beatae vitae dicta sunt explicabo.</p>
<div class="email">Enter Your Email</div>
<a class="btn" style="left:528px;top:3375px;width:144px;height:52px">SUBMIT</a>

<footer class="footer"></footer>
<div class="abs" style="left:0;width:1200px;top:3560px;display:flex;flex-direction:column;align-items:center;gap:14px">
  <div style="width:90px;height:90px;border-radius:50%;border:4px solid #fff"></div>
  <div style="font-size:38px;font-weight:700;color:#fff">Vetora</div>
</div>
<div class="foot-nav" style="left:310px">HOME</div>
<div class="foot-nav" style="left:415px">ABOUT US</div>
<div class="foot-nav" style="left:533px">SERVICES</div>
<div class="foot-nav" style="left:648px">COURSES</div>
<div class="foot-nav" style="left:749px">NEWS</div>
<div class="foot-nav" style="left:863px">CONTACT US</div>
<div class="social" style="left:496px"></div>
<div class="social" style="left:539px"></div>
<div class="social" style="left:581px"></div>
<div class="social" style="left:625px"></div>
<div class="social" style="left:667px"></div>
<p class="abs" style="left:0;width:1200px;top:3843px;text-align:center;color:#fff;font-size:14px">© Copyrights 2020-Vetora.All Rights Reserved.</p>

</body>
</html>
```